Bref créative
Larchmere Restoring LLC
Bringing new life to old wood
Professional
Trent Holloway
owner
larchmererestore@mailvox.net
I need the following listed on the card.
Owners:
Trent Holloway 555 274 1906
Darby Fennimore 555 381 4527
Licensed and Insured
Free Estimates.
Hardwood floors and Cabinets. If it's made of wood we can renew it. Color changes or tints. Low odor, dust, and mess. A fraction of the cost vs refacing or replacement. Quick turnaround. Most jobs completed in 1-2 days.

```html
<!DOCTYPE html>
<html lang="en">
<head>
<meta charset="utf-8">
<title>Larchmere Restoring LLC – Business Cards</title>
<link href="https://fonts.googleapis.com/css2?family=Open+Sans:wght@400;700&display=swap" rel="stylesheet">
<style>
  :root{
    --page:#ffffff;
    --charcoal:#2a2a2a;
    --bronze-dark:#5a4128;
    --bronze-mid:#8b6c4b;
    --bronze-light:#b39474;
    --silver-light:#f4f4f4;
    --silver-mid:#d6d6d6;
    --silver-dark:#a9a9a9;
    --ink:#2b2b2b;
    --grey-text:#8a8a8a;
    --accent-bronze:#7a5a38;
    --white:#ffffff;
  }
  *{margin:0;padding:0;box-sizing:border-box}
  html,body{width:1200px;height:727px;overflow:hidden;background:var(--page)}
  body{position:relative;font-family:"Open Sans",Arial,sans-serif}
  .card{position:absolute;width:562px;height:331px;overflow:hidden}
  .card--owners{left:19px;top:24px;background:var(--charcoal)}
  .card--silver{left:600px;top:24px;background:linear-gradient(135deg,var(--silver-light),var(--silver-mid) 55%,var(--silver-dark))}
  .card--white{left:19px;top:367px;background:var(--white);border:1px solid #9a9a9a}
  .card--bronze{left:600px;top:367px;background:linear-gradient(120deg,var(--bronze-mid),var(--bronze-dark) 45%,var(--bronze-light))}
  .card-bg{position:absolute;inset:0}

  .mark{display:block;background:linear-gradient(135deg,var(--bronze-light),var(--bronze-dark));border:2px solid var(--silver-mid)}
  .brand{position:absolute;display:flex;align-items:center;gap:10px}
  .brand-name{font-weight:700;text-transform:uppercase;letter-spacing:.06em;line-height:1.15}

  .card--owners .brand{left:22px;top:26px}
  .card--owners .mark{width:66px;height:66px}
  .card--owners .brand-name{color:var(--white);font-size:13px;width:150px}
  .owners-title{position:absolute;left:150px;top:138px;color:var(--white);font-size:25px}
  .owners-list{position:absolute;right:22px;top:200px;text-align:right;color:var(--white);font-size:15px;line-height:1.35}
  .owners-email{position:absolute;right:22px;top:265px;color:var(--white);font-size:15px}
  .owners-footer{position:absolute;left:22px;bottom:16px;color:var(--white);font-size:15px}

  .tagline{font-weight:700;font-size:23px}
  .services{font-size:20px;line-height:1.32}

  .card--silver .tagline{position:absolute;left:28px;top:36px;color:var(--ink)}
  .card--silver .brand{right:26px;top:20px;flex-direction:column;gap:4px}
  .card--silver .mark{width:96px;height:96px}
  .card--silver .brand-name{color:var(--ink);font-size:9px;text-align:center}
  .card--silver .services{position:absolute;left:28px;top:140px;width:500px;color:var(--ink)}

  .card--white .brand{left:0;right:0;top:22px;flex-direction:column;gap:4px}
  .card--white .mark{width:86px;height:86px}
  .card--white .brand-name{color:var(--accent-bronze);font-size:9px}
  .card--white .tagline{position:absolute;left:0;right:0;top:140px;text-align:center;color:var(--accent-bronze);font-size:20px}
  .card--white .services{position:absolute;left:30px;right:30px;top:176px;text-align:center;color:var(--grey-text);font-size:19px;line-height:1.3}

  .card--bronze .tagline{position:absolute;left:28px;top:26px;color:var(--white)}
  .card--bronze .services{position:absolute;left:28px;top:78px;width:500px;color:var(--white)}
  .card--bronze .brand{right:22px;bottom:18px}
  .card--bronze .mark{width:54px;height:54px}
  .card--bronze .brand-name{color:var(--white);font-size:12px;width:120px}
</style>
</head>
<body>

<section class="card card--owners">
  <svg class="card-bg" width="562" height="331" viewBox="0 0 562 331" aria-hidden="true">
    <defs>
      <linearGradient id="bronzeSweep" x1="0" y1="0" x2="1" y2="1">
        <stop offset="0" stop-color="#a88a69"/>
        <stop offset=".5" stop-color="#6b4f33"/>
        <stop offset="1" stop-color="#9c7d5c"/>
      </linearGradient>
      <linearGradient id="silverSweep" x1="0" y1="0" x2="1" y2="1">
        <stop offset="0" stop-color="#f2f2f2"/>
        <stop offset="1" stop-color="#a8a8a8"/>
      </linearGradient>
    </defs>
    <rect width="562" height="331" fill="url(#bronzeSweep)"/>
    <polygon points="0,0 362,0 300,331 0,331" fill="#2a2a2a"/>
    <polygon points="362,0 470,0 318,230 300,331" fill="url(#silverSweep)"/>
  </svg>
  <div class="brand"><span class="mark"></span><span class="brand-name">Larchmere<br>Restoring LLC</span></div>
  <h2 class="owners-title">Owners</h2>
  <p class="owners-list">Trent Holloway 555 274 1906<br>Darby Fennimore 555 381 4527</p>
  <p class="owners-email">Email: larchmererestore@mailvox.net</p>
  <p class="owners-footer">Licensed and Insured Free Estimates.</p>
</section>

<section class="card card--silver">
  <p class="tagline">"Bringing new life to old wood."</p>
  <div class="brand"><span class="mark"></span><span class="brand-name">Larchmere Restoring LLC</span></div>
  <p class="services">Hardwood floors and Cabinets. If it's made of wood we can renew it. Color changes or tints. Low odor, dust, and mess. A fraction of the cost vs refacing or replacement. Quick turnaround.<br>&nbsp;Most jobs completed in 1-2 days.</p>
</section>

<section class="card card--white">
  <div class="brand"><span class="mark"></span><span class="brand-name">Larchmere Restoring LLC</span></div>
  <p class="tagline">"Bringing new life to old wood."</p>
  <p class="services">Hardwood floors and Cabinets. If it's made of wood we can renew it. Color changes or tints. Low odor, dust, and mess. A fraction of the cost vs refacing or replacement. Quick turnaround.<br>Most jobs completed in 1-2 days.</p>
</section>

<section class="card card--bronze">
  <p class="tagline">"Bringing new life to old wood."</p>
  <p class="services">Hardwood floors and Cabinets. If it's made of wood we can renew it. Color changes or tints. Low odor, dust, and mess. A fraction of the cost vs refacing or replacement. Quick turnaround.<br>&nbsp;Most jobs completed in 1-2 days.</p>
  <div class="brand"><span class="mark"></span><span class="brand-name">Larchmere<br>Restoring LLC</span></div>
</section>

</body>
</html>
```